Business Card Design

We are a design build firm specializing in the construction and design of kitchens. We are a "green" company, hence the logo. Here are some IDEAS we came up with. I am asking to use this for every person in our firm, so I will need to be able to edit the text. On the back, I am thinking of a very simple design... maybe carry over the white band around the edge. Maybe a simple saying on the back "Reshaping homes from First Sketch to Final Detail".

Please see our current website for our style and design info
www.cabinetrefitexample.com (going to be forwarded to pinelanternllc.com)

Industry/Entity Type

Construction

Contact Information for Business Card

Pine Lantern Design & Construction
Moira Faddenby - Chief Designer
418 Willow Bend
Maple Ford, CT 06712
203.555.0147 C
203.555.0192 O
www.pinelanternllc.com
plcabinets@mailbox.example

```html
<!DOCTYPE html>
<html lang="en">
<head>
<meta charset="utf-8">
<title>Pine Lantern Design &amp; Construction — Business Card</title>
<link rel="stylesheet" href="https://fonts.googleapis.com/css2?family=Source+Sans+3:wght@400;600;700&family=Merriweather:wght@300;400&display=swap">
<style>
  :root {
    --canvas-bg: #e9e7e3;
    --card-white: #ffffff;
    --card-black: #0b0b0b;
    --ink: #2b2b2b;
    --ink-dark: #1d2418;
    --leaf-green: #8cc63f;
    --rule: #c9c9c9;
    --sans: "Source Sans 3", Arial, sans-serif;
    --serif: "Merriweather", Georgia, serif;
  }
  * { box-sizing: border-box; margin: 0; padding: 0; }
  html, body { width: 1200px; height: 455px; overflow: hidden; }
  body { background: var(--canvas-bg); font-family: var(--sans); position: relative; }

  .card {
    position: absolute;
    top: 80px;
    width: 510px;
    height: 295px;
    box-shadow: 0 4px 14px rgba(0,0,0,.18);
    overflow: hidden;
  }
  .card--front { left: 50px; background: var(--card-white); }
  .card--back  { left: 640px; background: var(--card-black); }

  /* brand name block */
  .brand {
    position: absolute;
    left: 0; right: 0;
    display: flex;
    justify-content: center;
    align-items: center;
    gap: 12px;
  }
  .brand__dot {
    width: 26px; height: 26px;
    border-radius: 50%;
    background: var(--leaf-green);
    flex: none;
  }
  .brand__name {
    font-weight: 700;
    text-transform: uppercase;
    letter-spacing: 2px;
    line-height: 1.15;
    text-align: left;
  }
  .brand__name span { display: block; }
  .card--front .brand { top: 40px; }
  .card--front .brand__name { color: var(--ink-dark); font-size: 22px; }
  .card--back .brand { top: 92px; }
  .card--back .brand__name { color: #ffffff; font-size: 28px; }

  /* front: person + contact */
  .person {
    position: absolute;
    top: 158px;
    right: 230px;
    text-align: right;
    color: var(--ink);
  }
  .person__name { color: var(--leaf-green); font-weight: 700; font-size: 17px; }
  .person__title { font-size: 14px; margin-top: 1px; }
  .person__address { font-size: 14px; margin-top: 14px; line-height: 1.2; }

  .divider {
    position: absolute;
    left: 293px;
    top: 152px;
    width: 1px;
    height: 100px;
    background: var(--rule);
  }

  .contact {
    position: absolute;
    left: 306px;
    top: 152px;
    list-style: none;
    font-size: 13.5px;
    color: var(--ink);
  }
  .contact li { display: flex; align-items: center; gap: 8px; height: 22px; }
  .contact svg { width: 12px; height: 12px; flex: none; fill: var(--ink); }

  .front-bands { position: absolute; left: 0; bottom: 0; width: 510px; height: 40px; }

  /* back: tagline */
  .tagline {
    position: absolute;
    left: 0; right: 0;
    top: 208px;
    text-align: center;
    color: #ffffff;
    font-family: var(--serif);
    font-weight: 400;
    font-size: 17px;
    letter-spacing: .3px;
  }
</style>
</head>
<body>

  <section class="card card--front" aria-label="Business card front">
    <div class="brand">
      <div class="brand__dot"></div>
      <div class="brand__name"><span>Pine Lantern</span><span>Design &amp; Construction</span></div>
    </div>

    <div class="person">
      <p class="person__name">Moira Faddenby</p>
      <p class="person__title">Chief Designer</p>
      <p class="person__address">418 Willow Bend Maple Ford<br>CT 06712</p>
    </div>

    <div class="divider"></div>

    <ul class="contact">
      <li>
        <svg viewBox="0 0 24 24" aria-hidden="true"><circle cx="12" cy="12" r="11" fill="none" stroke="#2b2b2b" stroke-width="2"/><path d="M8 6h3l1 3-2 1a8 8 0 0 0 4 4l1-2 3 1v3c-6 1-11-4-10-10z"/></svg>
        203.555.0192
      </li>
      <li>
        <svg viewBox="0 0 24 24" aria-hidden="true"><path d="M7 1h10a2 2 0 0 1 2 2v18a2 2 0 0 1-2 2H7a2 2 0 0 1-2-2V3a2 2 0 0 1 2-2zm0 3v12h10V4zm5 14a1.5 1.5 0 1 0 0 3 1.5 1.5 0 0 0 0-3z"/></svg>
        203.555.0147
      </li>
      <li>
        <svg viewBox="0 0 24 24" aria-hidden="true"><path d="M2 9l10-7 10 7v12H2zm2 1.5V19h16v-8.5l-8 5.5z"/></svg>
        plcabinets@mailbox.example
      </li>
      <li>
        <svg viewBox="0 0 24 24" aria-hidden="true"><path d="M12 1a11 11 0 1 0 0 22 11 11 0 0 0 0-22zm-1 2.1V7H7.3A9 9 0 0 1 11 3.1zm2 0A9 9 0 0 1 16.7 7H13zM5.9 9H11v2H3.1a9 9 0 0 1 2.8-2zm7.1 0h5.1a9 9 0 0 1 2.8 2H13zM3.1 13H11v2H5.9a9 9 0 0 1-2.8-2zm9.9 0h7.9a9 9 0 0 1-2.8 2H13zm-5.7 4H11v3.9A9 9 0 0 1 7.3 17zm5.7 0h3.7a9 9 0 0 1-3.7 3.9z"/></svg>
        www.pinelanternllc.com
      </li>
    </ul>

    <svg class="front-bands" viewBox="0 0 510 40" preserveAspectRatio="none" aria-hidden="true">
      <defs>
        <linearGradient id="band-green" x1="0" x2="1" y1="0" y2="0">
          <stop offset="0" stop-color="#9bd23f"/>
          <stop offset="0.55" stop-color="#7cc129"/>
          <stop offset="1" stop-color="#2f4a12"/>
        </linearGradient>
      </defs>
      <polygon points="0,16 268,16 284,28 0,28" fill="#111"/>
      <polygon points="290,18 510,10 510,28 276,28" fill="url(#band-green)"/>
      <rect x="0" y="28" width="510" height="12" fill="#111"/>
    </svg>
  </section>

  <section class="card card--back" aria-label="Business card back">
    <div class="brand">
      <div class="brand__dot"></div>
      <div class="brand__name"><span>Pine Lantern</span><span>Design &amp; Construction</span></div>
    </div>
    <p class="tagline">Reshaping homes from First Sketch to Final Detail</p>
  </section>

</body>
</html>
```